Standard logo business card

We are seeking a solid, somewhat understated professional design. We are a tech company. We like fonts similar to Aptifer Slab. Front side will be white with the contact information and a small version of our primary (Light background) logo.

(We have three people so we will have three names and titles)

Back side will hold our reverse logo on dark background along with the tagline:

"Intelligent annotation solutions for complex data"

Target Market(s)

Professionals, Tech

Industry/Entity Type

Business

Contact Information for Business Card

Name
Title

Phone
Email
City, State
Website

[We will email leading designer specific contact information)

Font styles to use
Serif

Requirements
Must have
• Colors are:
• Orange RGB 245,92,23
• Blue RGB 3,34,56
Nice to have
• We like a split with the Name and Title on the right and then contact details (below) on the left.

```html
<!DOCTYPE html>
<html lang="en">
<head>
<meta charset="utf-8">
<title>Corvanta Business Card</title>
<link href="https://fonts.googleapis.com/css2?family=Ubuntu:wght@400;500;700&display=swap" rel="stylesheet">
<style>
  :root {
    --orange: rgb(245, 92, 23);
    --navy: rgb(3, 34, 56);
    --white: #ffffff;
    --ink-muted: #6b6f74;
    --ink: #2b3440;
    --backdrop: #1b1b1c;
  }
  * { box-sizing: border-box; margin: 0; padding: 0; }
  html, body {
    width: 1200px; height: 800px; overflow: hidden;
    background: var(--backdrop);
    font-family: "Ubuntu", sans-serif;
  }
  .stage {
    position: relative; width: 1200px; height: 800px;
    display: flex; align-items: center; justify-content: center; gap: 60px;
  }
  .card {
    position: relative; width: 520px; height: 300px; overflow: hidden;
  }
  .card--front { background: var(--white); }
  .card--back { background: var(--navy); }

  .brand {
    display: flex; align-items: center; gap: 10px;
    font-weight: 700; letter-spacing: -0.5px;
  }
  .brand__square { background: var(--orange); }

  .card--front .brand {
    position: absolute; left: 40px; top: 44px;
    font-size: 38px; color: var(--navy);
  }
  .card--front .brand__square { width: 22px; height: 22px; }

  .contact {
    position: absolute; left: 40px; top: 120px;
    list-style: none; font-size: 12px; line-height: 18px; color: var(--ink-muted);
  }
  .contact li { display: flex; align-items: center; gap: 8px; }
  .contact__icon { width: 12px; height: 12px; flex: none; }
  .contact__spacer { display: inline-block; width: 12px; }

  .person {
    position: absolute; right: 36px; top: 170px; text-align: left;
  }
  .person__name { font-size: 17px; font-weight: 700; color: var(--navy); }
  .person__title { font-size: 13px; color: var(--ink-muted); margin-top: 2px; }

  .band { position: absolute; left: 0; bottom: 0; width: 520px; height: 300px; }
  .website {
    position: absolute; right: 36px; bottom: 20px;
    font-size: 14px; color: var(--orange);
  }

  .card--back .brand-block {
    position: absolute; inset: 0;
    display: flex; flex-direction: column; align-items: center; justify-content: center; gap: 12px;
  }
  .card--back .brand { font-size: 44px; color: var(--white); }
  .card--back .brand__square { width: 24px; height: 24px; }
  .tagline { font-size: 12.5px; color: var(--white); letter-spacing: 0.2px; }
</style>
</head>
<body>
<main class="stage">
  <section class="card card--front" aria-label="Card front">
    <div class="brand"><span class="brand__square"></span><span>Corvanta</span></div>

    <ul class="contact">
      <li><span class="contact__spacer"></span>220 Commerce Way, Suite 300</li>
      <li><span class="contact__spacer"></span>Marlow, OH 44100</li>
      <li>
        <svg class="contact__icon" viewBox="0 0 12 12" aria-hidden="true">
          <path d="M2.5 1 L4.5 1 L5 3.5 L3.8 4.5 C4.5 6 6 7.5 7.5 8.2 L8.5 7 L11 7.5 L11 9.5 C11 10.3 10.3 11 9.5 11 C5 11 1 7 1 2.5 C1 1.7 1.7 1 2.5 1 Z" fill="var(--navy)"/>
        </svg>555-014-2273
      </li>
      <li>
        <svg class="contact__icon" viewBox="0 0 12 12" aria-hidden="true">
          <rect x="0.5" y="2" width="11" height="8" fill="var(--navy)"/>
          <path d="M1 2.5 L6 6.5 L11 2.5" stroke="var(--white)" stroke-width="1" fill="none"/>
        </svg>daniel@corvanta.com
      </li>
    </ul>

    <div class="person">
      <p class="person__name">Daniel Whitford</p>
      <p class="person__title">Managing Director</p>
    </div>

    <svg class="band" viewBox="0 0 520 300" aria-hidden="true">
      <path d="M0 286 L250 286 C276 286 274 244 302 244 L520 244 L520 300 L0 300 Z" fill="var(--navy)"/>
    </svg>
    <p class="website">www.corvanta.com</p>
  </section>

  <section class="card card--back" aria-label="Card back">
    <div class="brand-block">
      <div class="brand"><span class="brand__square"></span><span>Corvanta</span></div>
      <p class="tagline">Intelligent annotation solutions for complex data</p>
    </div>
  </section>
</main>
</body>
</html>
```